kiPlume Landing Page 2

Edit the attached page to make it more visually appealing and professional. This page is a landing page that will direct our viewers to our rallyvant page. The join buttons definitely need to be changed, as well as fonts for the whole page. Please put rallyvant logo on the "join us" button, and put chatterpod and blipster with logos on the bottom center. If there are any further questions please ask us. http://kiplume.moravist.com/hands.html

Target Market(s)

Middle class Americans ages 20-35.

Industry/Entity Type

It Professional

```html
<!DOCTYPE html>
<html lang="en">
<head>
<meta charset="utf-8">
<title>kiPlume — You are the change you seek</title>
<link rel="stylesheet" href="https://fonts.googleapis.com/css2?family=Source+Sans+3:wght@400;600;700&display=swap">
<style>
  :root {
    --header-top: #fbfbfb;
    --header-bottom: #e9e9e9;
    --logo-ink: #4a4a4a;
    --hero-dark: #1e1a17;
    --hero-mid: #4a423b;
    --hero-light: #6a6158;
    --text-light: #ffffff;
    --frame: #ffffff;
    --video-dark: #2a2a2a;
    --video-light: #7a7a7a;
    --button-top: #ffd35a;
    --button-bottom: #f59a12;
    --button-edge: #b8630a;
    --button-ink: #5a2a05;
    --footer-top: #33333b;
    --footer-bottom: #22222a;
    --footer-base: #141416;
    --footer-divider: #111114;
    --footer-divider-light: #45454d;
    --stripe-red: #c0282d;
    --stripe-blue: #3a7fc4;
    --footer-ink: #f2f2f2;
  }
  * { box-sizing: border-box; margin: 0; padding: 0; }
  html, body { width: 1200px; height: 768px; overflow: hidden; background: var(--footer-base); }
  body { font-family: "Source Sans 3", "Myriad Pro", Arial, sans-serif; position: relative; }

  .site-header {
    position: absolute; left: 0; top: 0; width: 1200px; height: 68px;
    background: linear-gradient(var(--header-top), var(--header-bottom));
    z-index: 2;
  }
  .site-header__edge { position: absolute; left: 0; bottom: -4px; width: 1200px; height: 5px; }
  .brand {
    position: absolute; left: 22px; top: 11px;
    font-size: 44px; font-weight: 700; color: var(--logo-ink); letter-spacing: -0.5px; line-height: 1;
  }

  .hero {
    position: absolute; left: 0; top: 68px; width: 1200px; height: 610px;
    background:
      radial-gradient(ellipse 55% 60% at 65% 55%, var(--hero-light), transparent 70%),
      radial-gradient(ellipse 40% 50% at 15% 45%, var(--hero-mid), transparent 75%),
      linear-gradient(160deg, var(--hero-mid), var(--hero-dark));
    text-align: center; color: var(--text-light);
  }
  .hero__title {
    position: absolute; left: 0; width: 1093px; top: 30px;
    font-size: 56px; font-weight: 700; letter-spacing: -0.3px; line-height: 1.2;
    text-shadow: 0 2px 6px rgba(0,0,0,.6);
  }
  .hero__lead {
    position: absolute; left: 0; width: 1097px; top: 97px;
    font-size: 34px; font-weight: 600; line-height: 1.2;
    text-shadow: 0 2px 5px rgba(0,0,0,.6);
  }

  .video-card {
    position: absolute; left: 369px; top: 189px; width: 453px; height: 285px;
    border: 5px solid var(--frame);
    background: radial-gradient(ellipse at 55% 50%, var(--video-light), var(--video-dark) 80%);
    display: flex; align-items: center; justify-content: center; gap: 17px;
    padding-top: 8px;
    color: var(--text-light); text-decoration: none;
    font-size: 35px; font-weight: 600;
    text-shadow: 0 1px 4px rgba(0,0,0,.7);
  }
  .video-card svg { width: 40px; height: 40px; }

  .join-button {
    position: absolute; left: 494px; top: 498px; width: 203px; height: 52px;
    border-radius: 6px;
    background: linear-gradient(var(--button-top), var(--button-bottom));
    box-shadow: 0 3px 0 var(--button-edge), 0 4px 8px rgba(0,0,0,.5);
    display: flex; align-items: center; justify-content: center; gap: 20px;
    padding-left: 4px;
    color: var(--button-ink); font-size: 28px; font-weight: 600; text-decoration: none;
  }
  .join-button__mark { width: 28px; height: 28px; border-radius: 4px; background: var(--button-ink); opacity: .85; }

  .site-footer {
    position: absolute; left: 0; top: 678px; width: 1200px; height: 62px;
    background: linear-gradient(var(--footer-top), var(--footer-bottom));
    border-bottom: 1px solid #000;
  }
  .site-footer__stripe {
    position: absolute; left: 0; top: 0; width: 1200px; height: 3px;
    background: linear-gradient(90deg,
      var(--stripe-red) 0 4%, var(--stripe-blue) 4% 17%, var(--stripe-red) 17% 30%,
      var(--stripe-blue) 30% 41%, var(--stripe-red) 41% 52%, var(--stripe-blue) 52% 72%,
      var(--stripe-red) 72% 78%, var(--stripe-blue) 78% 100%);
  }
  .social-links { position: absolute; right: 0; top: 3px; height: 59px; display: flex; list-style: none; }
  .social-links li { display: flex; }
  .social-links li + li { border-left: 1px solid var(--footer-divider); box-shadow: inset 1px 0 0 var(--footer-divider-light); }
  .social-links a {
    display: flex; align-items: center; gap: 10px; padding: 0 16px;
    color: var(--footer-ink); text-decoration: none; font-size: 22px; font-weight: 600;
  }
  .social-links li:first-child a { padding-left: 0; }
  .social-links li:last-child a { padding-right: 34px; }
  .social-links__mark { width: 20px; height: 20px; border-radius: 50%; background: var(--footer-ink); }
  .footer-base { position: absolute; left: 0; top: 741px; width: 1200px; height: 27px; background: var(--footer-base); }
</style>
</head>
<body>
  <header class="site-header">
    <div class="brand">kiPlume</div>
    <svg class="site-header__edge" viewBox="0 0 1200 5" preserveAspectRatio="none" aria-hidden="true">
      <pattern id="zigzag" width="6" height="5" patternUnits="userSpaceOnUse">
        <path d="M0 0 L3 4 L6 0 Z" fill="#e9e9e9"/>
      </pattern>
      <rect width="1200" height="5" fill="url(#zigzag)"/>
    </svg>
  </header>

  <main class="hero" role="img" aria-label="Sepia photograph of weathered hands cupped together">
    <h1 class="hero__title">You are the change you seek.</h1>
    <p class="hero__lead">Protecting your family and your future requires your action.</p>

    <a class="video-card" href="#video" role="img" aria-label="Video still of two worn hands held together">
      <svg viewBox="0 0 40 40" aria-hidden="true">
        <circle cx="20" cy="20" r="17.5" fill="none" stroke="#fff" stroke-width="2.5"/>
        <path d="M16 13 L27 20 L16 27 Z" fill="#fff"/>
      </svg>
      <span>Watch video</span>
    </a>

    <a class="join-button" href="#join">
      <span>Join Now</span>
      <span class="join-button__mark" aria-hidden="true"></span>
    </a>
  </main>

  <footer class="site-footer">
    <div class="site-footer__stripe"></div>
    <ul class="social-links">
      <li><a href="#chatterpod"><span class="social-links__mark"></span>chatterpod</a></li>
      <li><a href="#rallyvant"><span class="social-links__mark"></span>rallyvant</a></li>
      <li><a href="#blipster"><span class="social-links__mark"></span>blipster</a></li>
    </ul>
  </footer>
  <div class="footer-base"></div>
</body>
</html>
```